Velmora Biz Card 2019

New business card for Velmora Property Inspections. We are a residential home inspection company in Arizona.

Target Market(s)

Real Estate

Font styles to use
Sans Serif

Requirements
Must have
• Glen Mirewick
• Home Inspector
• Velmora Property Inspections, LLC
• 480-555-0172
• glen@velmora-llc.example

```html
<!DOCTYPE html>
<html lang="en">
<head>
<meta charset="utf-8">
<title>Velmora Biz Card 2019</title>
<link href="https://fonts.googleapis.com/css2?family=Lato:wght@400;700&display=swap" rel="stylesheet">
<style>
  :root {
    --backdrop: #d9d9d9;
    --card-dark: #2a2a2a;
    --card-light: #f4f5f6;
    --brand-green: #3db54a;
    --ink-grey: #666669;
    --rule-grey: #d2d4d6;
    --white: #f2f2f2;
  }
  * { margin: 0; padding: 0; box-sizing: border-box; }
  html, body { width: 1200px; height: 1200px; overflow: hidden; }
  body {
    background: var(--backdrop);
    font-family: "Lato", Arial, sans-serif;
    position: relative;
  }
  .card {
    position: absolute;
    left: 250px;
    width: 708px;
    height: 404px;
  }
  .card--front {
    top: 144px;
    background: var(--card-dark);
    display: flex;
    align-items: center;
    justify-content: center;
  }
  .card--back {
    top: 582px;
    background: var(--card-light);
  }
  .wordmark {
    display: flex;
    align-items: center;
    gap: 14px;
    font-weight: 700;
    letter-spacing: 3px;
  }
  .wordmark__square {
    width: 22px;
    height: 22px;
    background: var(--brand-green);
  }
  .card--front .wordmark { font-size: 46px; color: var(--white); }
  .card--back .wordmark {
    position: absolute;
    left: 112px;
    top: 198px;
    font-size: 36px;
    color: var(--ink-grey);
  }
  .card--back .wordmark__square { width: 18px; height: 18px; }
  .divider {
    position: absolute;
    left: 354px;
    top: 130px;
    width: 1px;
    height: 120px;
    background: var(--rule-grey);
  }
  .contact {
    position: absolute;
    left: 374px;
    top: 103px;
    color: var(--ink-grey);
    font-size: 16.5px;
    line-height: 1.4;
  }
  .contact__name {
    color: var(--brand-green);
    font-weight: 700;
    font-size: 23px;
    line-height: 1.2;
  }
  .contact__title { margin-bottom: 12px; }
  .contact__company { color: var(--brand-green); }
  .contact__address { margin-bottom: 12px; }
  .contact__line { display: flex; align-items: center; gap: 8px; }
  .contact__line svg { width: 12px; height: 12px; fill: var(--brand-green); }
</style>
</head>
<body>
  <section class="card card--front">
    <div class="wordmark"><span class="wordmark__square"></span>VELMORA</div>
  </section>

  <section class="card card--back">
    <div class="wordmark"><span class="wordmark__square"></span>VELMORA</div>
    <div class="divider"></div>
    <div class="contact">
      <div class="contact__name">Glen Mirewick</div>
      <div class="contact__title">Home Inspector</div>
      <div class="contact__company">Velmora Property Inspections, LLC</div>
      <div class="contact__address">4410 S. Harlow Ave.<br>Tempe, AZ 85283</div>
      <div class="contact__line">
        <svg viewBox="0 0 24 24" aria-hidden="true"><path d="M6.6 10.8a15.2 15.2 0 0 0 6.6 6.6l2.2-2.2a1 1 0 0 1 1-.25 11.4 11.4 0 0 0 3.6.57 1 1 0 0 1 1 1V20a1 1 0 0 1-1 1A17 17 0 0 1 3 4a1 1 0 0 1 1-1h3.5a1 1 0 0 1 1 1c0 1.25.2 2.45.57 3.57a1 1 0 0 1-.25 1z"/></svg>
        <span>480-555-0172</span>
      </div>
      <div class="contact__line">
        <svg viewBox="0 0 24 24" aria-hidden="true"><path d="M2 5h20v14H2z M2 5l10 8 10-8" fill="var(--brand-green)"/><path d="M3 6l9 7 9-7" stroke="#f4f5f6" stroke-width="2" fill="none"/></svg>
        <span>glen@velmora-llc.example</span>
      </div>
    </div>
  </section>
</body>
</html>
```